Major Chiropractic Campaign Shown to 7 million people in print and online

Please design a SIMPLE and CLEAR advert in various sizes that will be used for print and media.

1/ Newspaper Print size: 381 x 272 with border and MUST be able to stand out in a newspaper

2/ Media: 5 sizes - rotating .gif 2 frames
- 160x600
- 728x90
- 300x250
- 300x600
- 320x50

3/ Facebook (must pass: http://tenthgridcheck.info)
- 300x315

Target Market(s)

females
35 - 54 yo
educated

Industry/Entity Type

Media

Font styles to use
Sans Serif

Colors
3176b5
33a6d7
ffffff
ec1f27
1b1b1b
919191
9bcb3c

Requirements
Must have
• clean
• easy to read
• strong CALL TO ACTION
• professional
• well designed book cover with the title " The Quiet Thread Linking Your Mind and Frame Revealed"
• The book MUST look like it's a professional report
• the winning design WILL show all design on a single page

```html
<!DOCTYPE html>
<html lang="en">
<head>
<meta charset="utf-8">
<title>Free Report – Banner Set</title>
<link rel="stylesheet" href="https://fonts.googleapis.com/css2?family=Questrial&family=Nunito:wght@800;900&family=Roboto+Condensed:wght@700&display=swap">
<style>
  :root{
    --blue:#3176b5;
    --sky:#33a6d7;
    --white:#ffffff;
    --red:#ec1f27;
    --ink:#1b1b1b;
    --stage:#8f8f8f;
    --green:#9bcb3c;
  }
  *{box-sizing:border-box;margin:0;padding:0}
  html,body{width:1200px;height:1000px;overflow:hidden;background:var(--stage)}
  .canvas{position:relative;width:1200px;height:1000px;font-family:"Questrial",sans-serif;color:var(--ink)}

  .ad{position:absolute;background:var(--green);overflow:hidden}
  .ad__badge{position:absolute;background:var(--red);color:var(--white);font-family:"Nunito",sans-serif;font-weight:900;line-height:1.05;text-align:center;display:flex;align-items:center;justify-content:center}
  .ad__band{position:absolute;left:0;right:0;background:var(--red)}
  .ad__headline{position:absolute;line-height:1.2}
  .ad__headline strong{font-weight:400;font-family:"Questrial",sans-serif;-webkit-text-stroke:.6px var(--ink)}

  .cta{position:absolute;display:flex;align-items:center;justify-content:center;border-radius:4px;
       background:linear-gradient(#ff6a4a,#e8321f 55%,#c81e12);box-shadow:0 2px 3px rgba(0,0,0,.35);
       font-family:"Roboto Condensed",sans-serif;font-weight:700;color:var(--ink);white-space:nowrap}

  /* report cover */
  .book{position:absolute;width:10em;height:13em;box-shadow:.35em .35em .6em rgba(0,0,0,.45);background:var(--white)}
  .book__spine{position:absolute;left:0;top:0;bottom:0;width:1.2em;background:var(--blue);display:flex;align-items:center;justify-content:center}
  .book__spine span{writing-mode:vertical-rl;text-orientation:upright;color:var(--white);font-family:"Nunito",sans-serif;font-weight:800;font-size:.6em;letter-spacing:.5em}
  .book__cover{position:absolute;left:1.2em;right:0;top:0;bottom:0;border:.22em solid var(--blue);border-left:0}
  .book__label{position:absolute;left:.4em;top:.4em;color:var(--blue);font-size:.62em;white-space:nowrap}
  .book__art{position:absolute;left:.2em;right:.2em;top:1.55em;height:6.4em;
       background:radial-gradient(circle at 50% 45%,#d9c2ff 0,#7b5cd6 18%,#1d4fa8 45%,#0a1a4a 80%)}
  .book__title{position:absolute;left:0;right:0;top:8.35em;text-align:center;color:var(--blue);line-height:1.1}
  .book__title .t1{display:block;font-size:.62em}
  .book__title .t2{display:block;font-size:.72em;font-weight:700;font-family:"Nunito",sans-serif}
  .book__title .t3{display:block;font-size:.4em;color:var(--ink)}
  .book__title .t4{display:block;font-size:.26em;color:var(--ink);margin-top:.6em;padding:0 .4em}
</style>
</head>
<body>
<div class="canvas">

  <!-- 728 x 90 -->
  <section class="ad" style="left:17px;top:34px;width:731px;height:92px">
    <div class="book" style="font-size:6.5px;left:13px;top:4px">
      <div class="book__spine"><span>Free Report</span></div>
      <div class="book__cover"><span class="book__label">FREE REPORT</span><div class="book__art" role="img" aria-label="Glowing brain artwork"></div>
        <p class="book__title"><span class="t1">THE QUIET THREAD</span><span class="t3">LINKING YOUR MIND AND FRAME</span></p></div>
    </div>
    <div class="book" style="font-size:4.2px;left:108px;top:24px">
      <div class="book__spine"><span>Free Report</span></div>
      <div class="book__cover"><span class="book__label">FREE REPORT</span><div class="book__art" role="img" aria-label="Glowing brain artwork"></div>
        <p class="book__title"><span class="t1">THE QUIET THREAD</span></p></div>
    </div>
    <p class="ad__headline" style="left:170px;top:14px;width:430px;text-align:right;font-size:24px">Doctors Explains Hidden Connection<br>that Control your <strong>Health</strong></p>
    <span class="cta" style="left:196px;top:52px;width:82px;height:21px;font-size:9px">GET FREE REPORT</span>
    <div class="ad__badge" style="left:615px;top:0;width:116px;height:92px;font-size:26px">Free<br>Report</div>
  </section>

  <!-- 320 x 50 -->
  <section class="ad" style="left:828px;top:54px;width:320px;height:51px">
    <div class="book" style="font-size:3.8px;left:2px;top:1px">
      <div class="book__spine"><span>Free</span></div>
      <div class="book__cover"><span class="book__label">FREE REPORT</span><div class="book__art" role="img" aria-label="Glowing brain artwork"></div></div>
    </div>
    <div class="book" style="font-size:2.6px;left:52px;top:15px">
      <div class="book__spine"><span>Free</span></div>
      <div class="book__cover"><div class="book__art" role="img" aria-label="Glowing brain artwork"></div></div>
    </div>
    <p class="ad__headline" style="left:80px;top:5px;width:185px;text-align:right;font-size:10.5px">Doctors Explains Hidden Connection<br>that Control your <strong>Health</strong></p>
    <span class="cta" style="left:79px;top:24px;width:52px;height:14px;font-size:6px;border-radius:2px">GET FREE REPORT</span>
    <div class="ad__badge" style="left:269px;top:0;width:51px;height:51px;font-size:13px">Free<br>Report</div>
  </section>

  <!-- 160 x 600 -->
  <section class="ad" style="left:22px;top:178px;width:162px;height:600px">
    <div class="ad__badge" style="left:0;top:0;width:162px;height:100px;font-size:30px">Free<br>Report</div>
    <div class="book" style="font-size:13px;left:14px;top:114px">
      <div class="book__spine"><span>Free Report</span></div>
      <div class="book__cover"><span class="book__label">FREE REPORT</span><div class="book__art" role="img" aria-label="Glowing brain artwork"></div>
        <p class="book__title"><span class="t1">THE QUIET THREAD</span><span class="t3">LINKING YOUR MIND AND FRAME</span><span class="t4">Doctors reveal the link that shapes your body and keeps you well</span></p></div>
    </div>
    <span class="cta" style="left:27px;top:339px;width:115px;height:30px;font-size:12px">GET FREE REPORT</span>
    <p class="ad__headline" style="left:21px;top:398px;font-size:15px;line-height:1.17">Doctors<br>Explains<br>Hidden<br>Connection<br>that<br>Control your<br><strong style="font-size:30px;line-height:1.4">Health</strong></p>
    <div class="ad__band" style="top:577px;height:23px"></div>
  </section>

  <!-- 300 x 600 -->
  <section class="ad" style="left:200px;top:178px;width:302px;height:600px">
    <div class="ad__badge" style="left:0;top:0;width:302px;height:100px;font-size:44px">Free Report</div>
    <div class="book" style="font-size:18px;left:52px;top:112px">
      <div class="book__spine"><span>Free Report</span></div>
      <div class="book__cover"><span class="book__label">FREE REPORT</span><div class="book__art" role="img" aria-label="Glowing brain artwork"></div>
        <p class="book__title"><span class="t1">THE QUIET THREAD</span><span class="t3">LINKING YOUR MIND AND FRAME</span><span class="t4">Doctors reveal the link that shapes your body and keeps you well</span></p></div>
    </div>
    <span class="cta" style="left:172px;top:382px;width:114px;height:30px;font-size:12px">GET FREE REPORT</span>
    <p class="ad__headline" style="left:0;top:425px;width:302px;text-align:center;font-size:24px;line-height:1.2">Doctors Explains<br>Hidden Connection<br>that&nbsp; Control your<br><strong style="font-size:48px;line-height:1.5">Health</strong></p>
    <div class="ad__band" style="top:577px;height:23px"></div>
  </section>

  <!-- 300 x 250 (A) -->
  <section class="ad" style="left:526px;top:182px;width:302px;height:315px">
    <div class="ad__badge" style="left:210px;top:0;width:92px;height:64px;font-size:21px">Free<br>Report</div>
    <div class="book" style="font-size:14px;left:14px;top:40px">
      <div class="book__spine"><span>Free Report</span></div>
      <div class="book__cover"><span class="book__label">FREE REPORT</span><div class="book__art" role="img" aria-label="Glowing brain artwork"></div>
        <p class="book__title"><span class="t1">THE QUIET THREAD</span><span class="t3">LINKING YOUR MIND AND FRAME</span></p></div>
    </div>
    <p class="ad__headline" style="left:169px;top:80px;font-size:19px;line-height:1.25">Doctors<br>Explains<br>Hidden<br>Connection<br>that<br>Control your<br><strong>Health</strong></p>
    <span class="cta" style="left:91px;top:265px;width:106px;height:27px;font-size:11px">GET FREE REPORT</span>
    <div class="ad__band" style="top:303px;height:12px"></div>
  </section>

  <!-- 300 x 250 (B) -->
  <section class="ad" style="left:856px;top:182px;width:301px;height:250px">
    <div class="ad__badge" style="left:0;top:0;width:65px;height:54px;font-size:15px">Free<br>Report</div>
    <div class="book" style="font-size:14px;left:132px;top:8px">
      <div class="book__spine"><span>Free Report</span></div>
      <div class="book__cover"><span class="book__label">FREE REPORT</span><div class="book__art" role="img" aria-label="Glowing brain artwork"></div>
        <p class="book__title"><span class="t1">THE QUIET THREAD</span><span class="t3">LINKING YOUR MIND AND FRAME</span></p></div>
    </div>
    <p class="ad__headline" style="left:25px;top:66px;font-size:15px;line-height:1.17">Doctors<br>Explains<br>Hidden<br>Connection<br>that<br>Control your<br><strong>Health</strong></p>
    <span class="cta" style="left:39px;top:206px;width:84px;height:21px;font-size:9px">GET FREE REPORT</span>
    <div class="ad__band" style="top:241px;height:9px"></div>
  </section>

  <!-- newspaper / large -->
  <section class="ad" style="left:533px;top:537px;width:590px;height:420px">
    <div class="ad__badge" style="left:479px;top:0;width:111px;height:90px;font-size:28px">Free<br>Report</div>
    <div class="book" style="font-size:25px;left:16px;top:50px">
      <div class="book__spine"><span>Free Report</span></div>
      <div class="book__cover"><span class="book__label">FREE REPORT</span><div class="book__art" role="img" aria-label="Glowing brain artwork"></div>
        <p class="book__title"><span class="t1">THE QUIET THREAD</span><span class="t3">LINKING YOUR MIND AND FRAME</span><span class="t4">Doctors reveal the link that shapes your body and keeps you well</span></p></div>
    </div>
    <p class="ad__headline" style="left:275px;top:100px;width:300px;text-align:center;font-size:37px;line-height:1.1">THE QUIET<br>THREAD<br><span style="font-size:18px">LINKING YOUR MIND AND FRAME</span></p>
    <p class="ad__headline" style="left:285px;top:235px;font-size:22px;line-height:1.18">Doctors Explains<br>Hidden Connection<br>that Control your<br><strong>Health</strong></p>
    <span class="cta" style="left:422px;top:329px;width:109px;height:29px;font-size:12px">GET FREE REPORT</span>
    <div class="ad__band" style="top:395px;height:25px;color:var(--white);font-size:13px;text-align:center;line-height:25px">www.seemoreinside.com.au</div>
  </section>

</div>
</body>
</html>
```